Web Design For Staffing Company

We need a homepage web design for a technical staffing company.

Please see attached brief for project details.

please make the site modern with bold colors while matching the logo

Be sure to read the attached breif in full beforehand.

Target Market(s)

technical companies looking to hire talent

Industry/Entity Type

Staffing

Number of Pages Required

1 page

Font styles to use
Sans Serif

```html
<!DOCTYPE html>
<html lang="en">
<head>
<meta charset="utf-8">
<title>Vantora Staffing — Technical Staffing</title>
<link href="https://fonts.googleapis.com/css2?family=Montserrat:wght@700&family=Poppins:wght@300;400;500&family=Crimson+Text&display=swap" rel="stylesheet">
<style>
  :root {
    --hero-dark: #1e3550;
    --hero-mid: #4a6784;
    --hero-light: #8aa2b8;
    --accent: #3d98e0;
    --accent-deep: #1f6fc0;
    --band-top: #2b90f0;
    --band-bottom: #1565c8;
    --white: #ffffff;
    --muted: #9aa4ae;
  }
  * { box-sizing: border-box; margin: 0; padding: 0; }
  html, body { width: 1200px; height: 707px; overflow: hidden; }
  body { font-family: "Poppins", sans-serif; color: var(--white); position: relative; background: var(--hero-dark); }

  .hero { position: absolute; left: 0; top: 0; width: 1200px; height: 614px; }
  .hero-photo {
    position: absolute; inset: 0;
    background:
      radial-gradient(ellipse at 72% 55%, rgba(170,190,210,.55), transparent 55%),
      radial-gradient(ellipse at 25% 30%, rgba(80,105,135,.6), transparent 60%),
      linear-gradient(135deg, var(--hero-mid) 0%, var(--hero-dark) 45%, var(--hero-light) 100%);
  }

  .brand { position: absolute; left: 215px; top: 24px; display: flex; align-items: center; gap: 8px; }
  .brand-mark { width: 14px; height: 14px; border-radius: 50%; background: var(--accent); }
  .brand-name { font-family: "Poppins", sans-serif; font-weight: 500; font-size: 18px; color: var(--white); letter-spacing: .5px; }

  .main-nav { position: absolute; top: 35px; left: 597px; display: flex; gap: 0; }
  .main-nav a { color: var(--white); text-decoration: none; font-size: 11.5px; font-weight: 400; letter-spacing: .6px; margin-right: 33px; }

  .hero-title {
    position: absolute; top: 296px; left: 0; width: 1200px; text-align: center;
    font-family: "Montserrat", sans-serif; font-weight: 700; font-size: 39px; line-height: 50px;
  }
  .hero-subtitle {
    position: absolute; top: 351px; left: 0; width: 1200px; text-align: center;
    font-family: "Crimson Text", serif; font-size: 24px; line-height: 32px;
  }

  .cta { position: absolute; top: 410px; height: 37px; width: 107px; display: flex; align-items: center; justify-content: center;
    font-size: 11px; letter-spacing: .7px; color: var(--white); text-decoration: none; border-radius: 2px; }
  .cta-hire { left: 485px; background: var(--accent); }
  .cta-get { left: 609px; background: var(--accent-deep); }

  .job-search { position: absolute; left: 254px; top: 504px; width: 696px; height: 47px; background: var(--white); border-radius: 3px; display: flex; overflow: hidden; }
  .field { display: flex; align-items: center; gap: 10px; padding-left: 15px; color: var(--muted); font-size: 9.5px; }
  .field-keywords { width: 346px; border-right: 1px solid #e3e6ea; }
  .field-location { width: 217px; }
  .find-btn { flex: 1; background: var(--accent); color: var(--white); display: flex; align-items: center; justify-content: center;
    font-family: "Montserrat", sans-serif; font-weight: 700; font-size: 11px; letter-spacing: 2px; }
  .advanced-link { position: absolute; left: 832px; top: 556px; font-size: 10.5px; font-weight: 500; letter-spacing: .6px; color: var(--white); }

  .info-band { position: absolute; left: 0; top: 614px; width: 1200px; height: 93px; background: linear-gradient(var(--band-top), var(--band-bottom)); }
  .info-item { position: absolute; top: 24px; width: 260px; margin-left: -130px; text-align: center; }
  .info-item h2 { font-family: "Montserrat", sans-serif; font-weight: 700; font-size: 15.5px; letter-spacing: .4px; }
  .info-item p { font-size: 16px; font-weight: 300; margin-top: 7px; letter-spacing: .3px; }
</style>
</head>
<body>
  <header class="hero">
    <div class="hero-photo" role="img" aria-label="Photo of hands typing on a laptop over architectural blueprints, with pens and a phone on the desk, under a blue overlay"></div>

    <div class="brand"><span class="brand-mark"></span><span class="brand-name">Vantora Staffing</span></div>

    <nav class="main-nav">
      <a href="#">HOME</a><a href="#">ABOUT</a><a href="#">JOB SEEKERS</a><a href="#">CLIENTS</a><a href="#">CONTACT</a>
    </nav>

    <h1 class="hero-title">The Right People For The Right Jobs!</h1>
    <p class="hero-subtitle">Bridging the talent gap in Technical Staffing</p>

    <a class="cta cta-hire" href="#">HIRE TALENT</a>
    <a class="cta cta-get" href="#">GET HIRED</a>

    <form class="job-search">
      <div class="field field-keywords">
        <svg width="17" height="17" viewBox="0 0 17 17" fill="none" stroke="#9aa4ae" stroke-width="1.3"><circle cx="7" cy="7" r="5.5"/><line x1="11" y1="11" x2="16" y2="16"/></svg>
        <span>Job title, skills, or company</span>
      </div>
      <div class="field field-location">
        <svg width="12" height="17" viewBox="0 0 12 17" fill="none" stroke="#9aa4ae" stroke-width="1.2"><path d="M6 16C2.5 11 1 8.5 1 6a5 5 0 0 1 10 0c0 2.5-1.5 5-5 10z"/><circle cx="6" cy="6" r="2"/></svg>
        <span>City, state or zip</span>
      </div>
      <div class="find-btn">FIND JOBS</div>
    </form>
    <a class="advanced-link">Advanced search</a>
  </header>

  <section class="info-band">
    <div class="info-item" style="left:322px"><h2>CALL US 24/7</h2><p>+123-4560-7890</p></div>
    <div class="info-item" style="left:613px"><h2>EMAIL US</h2><p>info@vantorastaffing.com</p></div>
    <div class="info-item" style="left:860px"><h2>OPEN HOURS</h2><p>Daily: 9:00-20:00</p></div>
  </section>
</body>
</html>
```